Label Design for a sexy ladies 5 pocket skinny

We need modern packaging design for women's skinny 5 pocket pants for a brand name Tarnel. All kinds of packaging designs are welcome.
The pant is folded and packaged in a poly bag. We require a label design for the brand name Tarnel. The main label will be attached by a string on the belt loop. the size of that label will 25cm in length and 10cm wide. This is the first label the customer see's when she picks up the garment. Therefore, we require an eye catching design for that. If required it could have certain information about the pant on the main label such as Comfort fit, Wrinkle-resistant, machine washable, luxury fabric. But, if you feel that adding the above information spoils the design of the label then it is not a must to include the above information. On the back of the label we like to include the information that this pant was manufactured in an Oskel Platinum certified green plant and hence the damage to the environment because of the plant is nill.
The second label is attached on to the waist band and the purpose of that label is to include the size of the pant such 32x32. The size of that label is 8cm in length and 4cm in width. There is no design on the back on this label it has to be blank.
Sample is given for what we currently use for our mens chino pant. we are looking for something very different.
Reason: because there was a delay in the project being approved by pixel harbor.
Environment

```html
<!DOCTYPE html>
<html lang="en">
<head>
<meta charset="utf-8">
<title>Tarnel – Hang Tag &amp; Size Label Concepts</title>
<link href="https://fonts.googleapis.com/css2?family=Arimo:wght@400;700&family=Josefin+Sans:wght@300;400&family=Montserrat:wght@500;600&family=Oswald:wght@300;400;500&display=swap" rel="stylesheet">
<style>
  :root{
    --taupe:#9c857a;
    --sand:#c4b59b;
    --slate:#555555;
    --ink:#050505;
    --paper:#ffffff;
    --wine:#590c31;
    --peach:#f2c896;
    --tan:#9a7551;
    --cream:#e8d9b5;
  }
  *{box-sizing:border-box;margin:0;padding:0}
  html,body{width:1200px;height:900px;overflow:hidden;background:var(--paper)}
  body{position:relative;font-family:"Arimo",Arial,sans-serif}
  .tag{position:absolute;overflow:hidden}
  .tag > *{position:absolute}
  .hole{width:13px;height:13px;border-radius:50%;border:3px solid #2b2b2b}
  .hole--light{border-color:var(--taupe)}
  .shadowed{box-shadow:5px 6px 6px rgba(0,0,0,.55)}
  .wordmark{white-space:nowrap;line-height:1}
  .wm-geo{font-family:"Montserrat",Arial,sans-serif;font-weight:500}
  .wm-cond{font-family:"Oswald",Arial,sans-serif;font-weight:300}
  .wm-bold{font-family:"Oswald",Arial,sans-serif;font-weight:500}
  .wm-thin{font-family:"Josefin Sans",Arial,sans-serif;font-weight:300}
  .sub{font-family:"Arimo",Arial,sans-serif;font-size:6px;white-space:nowrap;letter-spacing:.2px;line-height:1}
  .features{font-family:"Arimo",Arial,sans-serif;font-size:7px;line-height:1.3}
  .features--bold{font-weight:700;text-transform:uppercase;font-size:8px}
  .vertical{writing-mode:vertical-rl;transform:rotate(180deg);white-space:nowrap}
  .stack{display:flex;flex-direction:column;align-items:center;justify-content:space-between;font-family:"Oswald",Arial,sans-serif;font-weight:400;line-height:1}
  .size{font-family:"Arimo",Arial,sans-serif;font-size:8px;white-space:nowrap}
  .size--bold{font-weight:700}
</style>
</head>
<body>

<!-- Row 1 : main hang tags -->
<div class="tag" style="left:27px;top:36px;width:142px;height:354px;background:var(--taupe)">
  <span class="hole" style="left:64px;top:4px"></span>
  <div style="left:0;top:26px;width:128px;height:180px;background:var(--ink)"></div>
  <p class="features features--bold" style="left:13px;top:157px;color:var(--taupe)">Comfort fit<br>wrinkle- resistant.<br>machine washeble,<br>luxury fabric.</p>
  <div style="left:0;top:274px;width:142px;height:6px;background:var(--ink)"></div>
  <span class="wordmark wm-geo" style="left:7px;top:290px;font-size:28px;color:var(--ink)">TARNEL</span>
  <span class="sub" style="right:4px;top:324px;color:var(--ink)">LADIES SKINNY</span>
</div>

<div class="tag" style="left:202px;top:36px;width:142px;height:354px;background:var(--taupe)">
  <span class="hole" style="left:69px;top:4px"></span>
  <div style="left:11px;top:0;width:24px;height:250px;background:var(--ink)"></div>
  <p class="features features--bold vertical" style="left:13px;top:96px;height:150px;color:var(--paper);font-size:6.5px;line-height:1.25">Comfort fit wrinkle- resistant.<br>machine washeble,luxury fabric.</p>
  <span class="wordmark wm-cond" style="left:9px;top:304px;font-size:38px;color:var(--ink)">TARNEL</span>
  <span class="sub" style="left:24px;top:344px;color:var(--ink)">LADIES SKINNY</span>
</div>

<div class="tag" style="left:368px;top:39px;width:142px;height:354px;background:var(--sand)">
  <span class="hole hole--light" style="left:65px;top:1px"></span>
  <span class="wordmark wm-thin" style="left:19px;top:114px;font-size:26px;color:var(--taupe)">TARNEL</span>
  <span class="sub" style="left:58px;top:146px;color:var(--paper);font-weight:700">LADIES SKINNY</span>
  <p class="features features--bold" style="left:5px;top:311px;font-size:6px;color:var(--paper)">Comfort fit wrinkle- resistant.<br>machine washeble, luxury fabric.</p>
  <div style="left:0;top:329px;width:142px;height:7px;background:var(--taupe)"></div>
</div>

<div class="tag" style="left:529px;top:39px;width:142px;height:354px;background:var(--slate)">
  <span class="hole hole--light" style="left:65px;top:1px"></span>
  <span class="wordmark wm-thin" style="left:13px;top:112px;font-size:30px;color:var(--taupe)">TARNEL</span>
  <span class="sub" style="left:45px;top:147px;color:var(--paper);font-weight:700">LADIES SKINNY</span>
  <div style="left:50px;top:209px;width:42px;height:6px;background:var(--taupe)"></div>
  <p class="features features--bold" style="left:13px;top:271px;font-size:6px;color:var(--taupe)">Comfort fit wrinkle- resistant.<br>machine washeble, luxury fabric.</p>
</div>

<div class="tag" style="left:695px;top:39px;width:143px;height:354px;background:var(--slate)">
  <span class="hole hole--light" style="left:65px;top:1px"></span>
  <span class="wordmark wm-thin" style="left:3px;top:226px;font-size:35px;color:var(--taupe);letter-spacing:-1px">TARNEL</span>
  <span class="sub" style="right:3px;top:262px;color:var(--paper);font-weight:700;font-size:5px">LADIES SKINNY</span>
  <div style="left:10px;top:320px;width:88px;height:24px;background:var(--taupe)"></div>
  <p class="features" style="left:13px;top:322px;font-size:5.5px;color:#3a3a3a">Comfort Fit Wrinkle - Resistant ,<br>Machine washeble,<br>Laxury fabric</p>
</div>

<div class="tag shadowed" style="left:872px;top:40px;width:141px;height:352px;background:var(--paper);overflow:visible">
  <span class="hole hole--light" style="left:63px;top:0"></span>
  <span class="wordmark wm-geo" style="left:33px;top:82px;font-size:23px;color:var(--ink)">TARNEL</span>
  <div style="left:33px;top:107px;width:99px;height:4px;background:var(--ink)"></div>
  <span class="sub" style="left:33px;top:114px;color:var(--ink);font-size:5px;font-weight:700">LADIES SKINNY</span>
  <p class="features" style="left:4px;top:306px;font-size:6px;color:var(--ink);font-weight:700">Comfort Fit Wrinkle - Resistant ,<br>Machine washeble,<br>Laxury fabric</p>
  <div style="left:0;top:346px;width:141px;height:6px;background:var(--ink)"></div>
</div>

<div class="tag shadowed" style="left:1038px;top:40px;width:142px;height:352px;background:var(--paper);overflow:visible">
  <div style="left:14px;top:0;width:22px;height:115px;background:var(--taupe)"></div>
  <span class="wordmark wm-cond" style="left:34px;top:128px;font-size:84px;color:var(--taupe);letter-spacing:-3px;transform:scaleX(.5);transform-origin:left">TARNEL</span>
  <span class="sub" style="right:6px;top:214px;color:var(--taupe);font-weight:700">LADIES SKINNY</span>
  <div style="left:17px;top:246px;width:98px;height:1px;background:var(--taupe)"></div>
  <p class="features" style="left:17px;top:265px;font-size:8px;color:var(--taupe);line-height:1.25">Comfort Fit Wrinkle - Resistant ,<br>Machine washeble,<br>Laxury fabric</p>
</div>

<!-- Row 2 : main hang tags -->
<div class="tag" style="left:31px;top:430px;width:142px;height:354px;background:var(--taupe)">
  <div class="stack" style="left:60px;top:30px;width:26px;height:252px;font-size:32px;color:var(--cream)">
    <span>T</span><span>A</span><span>R</span><span>N</span><span>E</span><span>L</span>
  </div>
  <div style="left:92px;top:31px;width:50px;height:255px;background:var(--ink)"></div>
  <p class="features features--bold vertical" style="left:104px;top:138px;height:144px;color:var(--paper);font-size:6.5px;line-height:1.25">Comfort fit wrinkle- resistant.<br>machine washeble,luxury fabric.</p>
  <div style="left:90px;top:290px;width:52px;height:10px;background:var(--ink)"></div>
  <span class="sub" style="left:93px;top:292px;color:var(--paper);font-weight:700;font-size:5px">LADIES SKINNY</span>
</div>

<div class="tag" style="left:202px;top:430px;width:142px;height:354px;background:var(--wine)">
  <div style="left:63px;top:0;width:15px;height:26px;background:var(--taupe)"></div>
  <span class="hole" style="left:64px;top:4px;border-color:var(--wine)"></span>
  <span class="wordmark wm-thin" style="left:24px;top:95px;font-size:24px;color:var(--taupe)">TARNEL</span>
  <div style="left:25px;top:139px;width:93px;height:1px;background:var(--taupe)"></div>
  <span class="sub" style="left:51px;top:158px;color:var(--taupe)">LADIES SKINNY</span>
  <p class="features" style="left:8px;top:322px;font-size:5.5px;color:var(--cream)">Comfort Fit Wrinkle - Resistant ,<br>Machine washeble,<br>Laxury fabric</p>
</div>

<div class="tag" style="left:368px;top:430px;width:142px;height:354px;background:var(--ink)">
  <p class="features" style="left:13px;top:34px;font-size:8px;color:var(--cream)">Comfort Fit Wrinkle - Resistant ,<br>Machine washeble,<br>Laxury fabric</p>
  <span class="wordmark wm-cond" style="left:13px;top:192px;font-size:46px;color:var(--taupe);transform:scaleX(.6);transform-origin:left">TARNEL</span>
  <span class="sub" style="left:13px;top:240px;color:var(--taupe)">LADIES SKINNY</span>
</div>

<!-- Size labels -->
<div class="tag" style="left:534px;top:428px;width:112px;height:224px;background:var(--sand)">
  <span class="wordmark wm-cond" style="left:42px;top:18px;font-size:44px;color:var(--taupe);transform:scaleX(.56);transform-origin:left">TARNEL</span>
  <span class="size" style="left:43px;top:191px;color:var(--ink)">SIZE:32</span>
</div>

<div class="tag" style="left:659px;top:428px;width:112px;height:224px;background:var(--ink)">
  <span class="wordmark wm-thin" style="left:4px;top:74px;font-size:27px;color:var(--taupe);letter-spacing:-1px">TARNEL</span>
  <span class="size" style="left:42px;top:195px;color:var(--cream)">SIZE:32</span>
</div>

<div class="tag" style="left:787px;top:428px;width:112px;height:224px;background:var(--slate)">
  <span class="wordmark wm-thin" style="left:5px;top:108px;font-size:25px;color:var(--taupe)">TARNEL</span>
  <span class="size size--bold" style="left:39px;top:201px;color:var(--cream)">SIZE:32</span>
</div>

<div class="tag" style="left:926px;top:428px;width:112px;height:224px;background:var(--taupe)">
  <div style="left:31px;top:0;width:50px;height:224px;background:var(--ink)"></div>
  <div class="stack" style="left:44px;top:16px;width:24px;height:180px;font-size:22px;color:var(--cream)">
    <span>T</span><span>A</span><span>R</span><span>N</span><span>E</span><span>L</span>
  </div>
  <span class="size" style="left:43px;top:206px;color:var(--paper)">SIZE:32</span>
</div>

<div class="tag" style="left:1061px;top:428px;width:112px;height:224px;background:var(--peach)">
  <span class="wordmark wm-cond" style="left:4px;top:22px;font-size:84px;color:var(--taupe);letter-spacing:-3px;transform:scaleX(.5);transform-origin:left">TARNEL</span>
  <span class="size" style="left:42px;top:202px;color:var(--taupe)">SIZE:32</span>
  <div style="left:0;top:217px;width:112px;height:6px;background:var(--taupe)"></div>
</div>

<div class="tag" style="left:534px;top:672px;width:225px;height:112px;background:var(--tan)">
  <span class="wordmark wm-bold" style="left:25px;top:38px;font-size:36px;color:var(--ink);transform:scaleX(.7);transform-origin:left">TARNEL</span>
  <span class="size size--bold" style="left:182px;top:57px;color:var(--cream)">SIZE:32</span>
</div>

<div class="tag" style="left:787px;top:672px;width:225px;height:112px;background:var(--slate)">
  <span class="wordmark wm-bold" style="left:14px;top:38px;font-size:36px;color:var(--paper);transform:scaleX(.7);transform-origin:left">TARNEL</span>
  <span class="size" style="left:181px;top:64px;color:var(--paper)">SIZE:32</span>
</div>

</body>
</html>
```